Webdesign  Seminare im Bereich persönliche Entwicklung, Spiritualität und Coaching
Webdesign Seminare im Bereich persönliche Entwicklung, Spiritualität und Coaching
Zielgruppe
Wir bieten Seminare im Bereich persönliche Entwicklung, Spiritualität und Coaching an. Unsere Zielgruppe umfasst Menschen zw. 18 und 75 jeglichen Berufsstandes, die sich dafür interessieren ihre tieferen innewohnenden Potenziale kennenzulernen und zu eröffnen.
Dieser Auftrag hier ist ein Teaser-Projekt. Wir wachsen konstant, möchten mehrere Folgeaufträge vergeben und suchen auf diesem Weg einen langfristigen Partner.
Aufgabenstellung
- keine esoterischen Klischee-Bilder, nichts Verspieltes
- unser Auftritt (hier vorerst die Website) soll wärmer wirken als dies aktuell der Fall ist, die Klarheit darf dabei jedoch nicht verloren gehen
- klar, warm, offen, vertraut, seriös
- das Logo darf verändert werden
Aktuell ist recht wenig Bildmaterial vorhanden. Hier wird demnächst nachproduziert. Bitte vorerst, wenn designtechnisch angebracht, Stockmaterial (als Platzhalter) verwenden.

```html
<!DOCTYPE html>
<html lang="de">
<head>
<meta charset="utf-8">
<title>AufbauWorkshops – KlarheitsRaum</title>
<link href="https://fonts.googleapis.com/css2?family=Poppins:wght@400;500;600&family=Playfair+Display:wght@500&display=swap" rel="stylesheet">
<style>
:root{
  --blue:#4ab0d3;
  --ink:#222;
  --text:#333;
  --line:#d9e9ef;
  --grey-line:#d6d6d6;
  --subnav:#f7f7f7;
  --white:#fff;
}
*{margin:0;padding:0;box-sizing:border-box}
html,body{width:746px;height:1200px;overflow:hidden;background:var(--white)}
body{position:relative;font-family:"Poppins",sans-serif;color:var(--text)}
.abs{position:absolute}
.topbar{left:0;top:0;width:746px;height:34px;background:var(--blue)}
.brand{left:139px;top:10px;color:var(--white);font-weight:600;font-size:10px;letter-spacing:.2px}
.mainnav{top:12px;right:139px;display:flex;gap:18px;font-size:6.4px;font-weight:600;color:var(--white)}
.mainnav .active{position:relative}
.mainnav .active::after{content:"";position:absolute;left:4px;right:4px;top:10px;height:.6px;background:var(--white)}
.subnav{left:0;top:34px;width:746px;height:22px;background:var(--subnav);display:flex;justify-content:center;gap:19px;font-size:6.4px;padding-top:6.5px;color:var(--ink)}
.subnav .current{color:var(--blue);position:relative;height:15.5px}
.subnav .current::after{content:"";position:absolute;left:0;right:0;bottom:0;height:1px;background:var(--blue)}
.hero{left:0;top:56px;width:746px;height:171px;background:linear-gradient(90deg,#cfae83 0%,#e3b47a 28%,#f4d9a4 50%,#f9ebc0 75%,#faf0cf 100%)}
.hero-title{right:139px;top:123px;font-family:"Playfair Display",serif;font-weight:500;font-size:20px;color:var(--ink)}
.hero-rule{left:574px;top:149px;width:33px;height:.8px;background:var(--ink)}
.card{left:139px;width:468px;background:var(--white);box-shadow:0 1px 4px rgba(0,0,0,.12);border-radius:2px;overflow:hidden}
.dates{top:273px;height:325px}
.card-head{height:25px;background:var(--blue);color:var(--white);font-size:6.4px;font-weight:600;position:relative}
.card-head span{position:absolute;top:8.5px}
.row{position:relative;height:62px;font-size:6.3px;line-height:9.4px}
.row + .row::before{content:"";position:absolute;left:12px;right:12px;top:0;height:.5px;background:var(--line)}
.row div{position:absolute;top:12px}
.c1{left:12px}.c2{left:100px}.c3{left:188px;width:108px}.c4{left:342px;color:var(--blue);font-weight:500}
.btn{left:393px;top:12.5px!important;width:63px;height:17px;background:var(--blue);color:var(--white);font-size:6.4px;font-weight:500;display:flex;align-items:center;justify-content:center;gap:3px}
.note{right:139px;width:468px;text-align:right;font-size:4.4px;line-height:7.6px;color:#444}
.intro{left:139px;top:686px;width:468px;font-size:7.4px;line-height:9.6px;font-weight:600;color:var(--ink)}
.acc{left:139px;top:712px;width:468px}
.acc-item{position:relative;height:22.2px;border-bottom:.6px solid var(--grey-line);font-size:7.3px;color:var(--ink);padding:6.5px 0 0 12px}
.acc-item.blue{color:var(--blue)}
.acc-item.open{border-bottom:1px solid var(--blue)}
.acc-item svg{position:absolute;right:12px;top:6px}
.acc-body{font-size:6.3px;line-height:9.4px;padding:5.5px 12px 12px;border-bottom:.6px solid var(--grey-line);color:var(--ink)}
.acc-body p+p{margin-top:9.4px}
.times{top:1005px;height:126px}
.times .row{height:33.7px}
.times .row div{top:12px}
.times .t2{left:187px}
.footer{left:0;top:1178px;width:746px;height:22px;background:var(--blue);color:var(--white);font-size:5.3px}
.footer span{position:absolute;top:7.5px}
</style>
</head>
<body>
<header class="abs topbar">
  <div class="abs brand">KlarheitsRaum</div>
  <nav class="abs mainnav"><span class="active">Start</span><span>Jonas Albrecht</span><span>KlarheitsRaum</span><span>Termine</span><span>Blog</span><span>Kontakt</span></nav>
</header>
<nav class="abs subnav"><span>Übersicht</span><span>BasisWorkshop</span><span class="current">AufbauWorkshops</span><span>OnlineErlebnisAbend</span><span>LiveMeditationen</span><span>Einzelsitzungen</span></nav>

<div class="abs hero" role="img" aria-label="Stockfoto: Frau mit ausgebreiteten Armen im warmen Abendlicht"></div>
<h1 class="abs hero-title">AufbauWorksops</h1>
<div class="abs hero-rule"></div>

<section class="abs card dates">
  <div class="card-head"><span style="left:12px">Termin</span><span style="left:100px">Ort</span><span style="left:188px">Seminarhaus</span><span style="left:342px">Preis</span></div>
  <div class="row"><div class="c1">15. – 18.02.2022</div><div class="c2">Online</div><div class="c3">Die eigene Kraft erwecken<br>Findet über Meetly statt<br>Eine kurze Beschreibung<br>findest du hier</div><div class="c4">595,- €</div><div class="btn">Anmelden <svg width="8" height="6" viewBox="0 0 8 6"><path d="M0 3h7M4.5 .5 7 3 4.5 5.5" stroke="#fff" stroke-width=".8" fill="none"/></svg></div></div>
  <div class="row"><div class="c1">24. – 27.02.2022</div><div class="c2">Edertal<br>(Kassel)</div><div class="c3">Leichtigkeit, Lebensfreude,<br>Heilung des inneren Kindes<br>Seminarhaus Seeblick<br>www.seeblick-tagungshaus.de</div><div class="c4">645,- €</div><div class="btn">Anmelden <svg width="8" height="6" viewBox="0 0 8 6"><path d="M0 3h7M4.5 .5 7 3 4.5 5.5" stroke="#fff" stroke-width=".8" fill="none"/></svg></div></div>
  <div class="row"><div class="c1">07. – 10.03.2022</div><div class="c2">Kißlegg<br>(Bodensee)</div><div class="c3">Wahre Freiheit<br>Seminarhaus Morgenlicht<br>www.tagungshaus-<br>morgenlicht.de</div><div class="c4">645,- €</div><div class="btn">Anmelden <svg width="8" height="6" viewBox="0 0 8 6"><path d="M0 3h7M4.5 .5 7 3 4.5 5.5" stroke="#fff" stroke-width=".8" fill="none"/></svg></div></div>
  <div class="row" style="height:52.5px"><div class="c1">23. – 26.05.2022</div><div class="c2">Edertal<br>(Kassel)</div><div class="c3">Krieger, Kraft, Unbesiegbarkeit<br>Seminarhaus Seeblick<br>www.seeblick-tagungshaus.de</div><div class="c4">645,- €</div><div class="btn">Anmelden <svg width="8" height="6" viewBox="0 0 8 6"><path d="M0 3h7M4.5 .5 7 3 4.5 5.5" stroke="#fff" stroke-width=".8" fill="none"/></svg></div></div>
  <div class="row"><div class="c1">13. – 16.06.2022</div><div class="c2">Chieming<br>(Chiemsee)</div><div class="c3">Selbstliebe, Ganzheit, tiefer<br>Frieden Seminarhaus<br>Lindenhof www.lindenhof-<br>seminarhotel.de</div><div class="c4">645,- €</div><div class="btn">Anmelden <svg width="8" height="6" viewBox="0 0 8 6"><path d="M0 3h7M4.5 .5 7 3 4.5 5.5" stroke="#fff" stroke-width=".8" fill="none"/></svg></div></div>
</section>

<p class="abs note" style="top:610px">Alle Preise inkl. gesetzlich gültiger Mehrwertsteuer, bei Präsenzveranstaltungen zuzüglich Unterkunft und Verpflegung, eine Ratenzahlung ist möglich nach Vereinbarung.</p>
<p class="abs note" style="top:626px">Das Seminarhaus lässt Maskenatteste leider nur ganz bedingt gelten. Mit einem Maskenattest musst du dir für die Wege im Seminarhaus und für das Bedienen am Buffet einen Faceshield mitbringen und aufsetzen.</p>

<p class="abs intro">Um spezifische Themen und Entwicklungsbereiche noch intensiver und gezielter bearbeiten zu können, wurden die AufbauWorkshops entwickelt. Voraussetzung für die Teilnahme ist ein absolvierter BasisWorkshop.</p>

<section class="abs acc">
  <div class="acc-item blue open">Verbindung zum wahren Selbst und meine Bestimmung<svg width="10" height="10" viewBox="0 0 10 10"><circle cx="5" cy="5" r="4.5" fill="none" stroke="#4ab0d3" stroke-width=".6"/><path d="M2.6 5h4.8" stroke="#4ab0d3" stroke-width=".6"/></svg></div>
  <div class="acc-body">
    <p>Die Verbindung zum wahren Selbst erzeugt ein glückseliges Feuerwerk in deinem Körper, deinem Herz und deinem Geist. Du fühlst dich getragen, geleitet und richtig an dem Platz, an dem du dich befindest.</p>
    <p>Wir gehen energetisch so „hoch“, wie es möglich ist und etablieren und realisieren diese Energien in dir und deinem Körper. Einmal mehr verbinden wir somit die hohen geistigen Ebenen mit der physischen Welt.</p>
    <p>Bist du mit deinem wahren Selbst verbunden, so ist es leicht für dich deine wahre Bestimmung in diesem Leben oder für diesen Augenblick zu erkennen. Dies wird dich ankommen lassen in dir selbst und kann eine Neuausrichtung in deinem Leben zur Folge haben.</p>
  </div>
  <div class="acc-item blue">Selbstliebe, Ganzheit, tiefer Frieden<svg width="10" height="10" viewBox="0 0 10 10"><circle cx="5" cy="5" r="4.5" fill="none" stroke="#4ab0d3" stroke-width=".6"/><path d="M2.6 5h4.8M5 2.6v4.8" stroke="#4ab0d3" stroke-width=".6"/></svg></div>
  <div class="acc-item">Intensiv-Reinigung<svg width="10" height="10" viewBox="0 0 10 10"><circle cx="5" cy="5" r="4.5" fill="none" stroke="#222" stroke-width=".6"/><path d="M2.6 5h4.8M5 2.6v4.8" stroke="#222" stroke-width=".6"/></svg></div>
  <div class="acc-item">Das unendliche Potenzial in mir<svg width="10" height="10" viewBox="0 0 10 10"><circle cx="5" cy="5" r="4.5" fill="none" stroke="#222" stroke-width=".6"/><path d="M2.6 5h4.8M5 2.6v4.8" stroke="#222" stroke-width=".6"/></svg></div>
  <div class="acc-item">Krieger, Kraft, Unbesiegbarkeit<svg width="10" height="10" viewBox="0 0 10 10"><circle cx="5" cy="5" r="4.5" fill="none" stroke="#222" stroke-width=".6"/><path d="M2.6 5h4.8M5 2.6v4.8" stroke="#222" stroke-width=".6"/></svg></div>
  <div class="acc-item">Leichtigkeit, Lebensfreude - Heilung des Inneren Kindes<svg width="10" height="10" viewBox="0 0 10 10"><circle cx="5" cy="5" r="4.5" fill="none" stroke="#222" stroke-width=".6"/><path d="M2.6 5h4.8M5 2.6v4.8" stroke="#222" stroke-width=".6"/></svg></div>
  <div class="acc-item">Die eigene Kraft erwecken<svg width="10" height="10" viewBox="0 0 10 10"><circle cx="5" cy="5" r="4.5" fill="none" stroke="#222" stroke-width=".6"/><path d="M2.6 5h4.8M5 2.6v4.8" stroke="#222" stroke-width=".6"/></svg></div>
  <div class="acc-item" style="border-bottom:none">Wahre Freiheit<svg width="10" height="10" viewBox="0 0 10 10"><circle cx="5" cy="5" r="4.5" fill="none" stroke="#222" stroke-width=".6"/><path d="M2.6 5h4.8M5 2.6v4.8" stroke="#222" stroke-width=".6"/></svg></div>
</section>

<section class="abs card times">
  <div class="card-head"><span style="left:12px">Workshopzeiten</span></div>
  <div class="row"><div class="c1">1. Tag</div><div class="t2">15.00 – 18.30 Uhr</div></div>
  <div class="row"><div class="c1" style="left:14px">2. – 3. Tag</div><div class="t2">09.00 – 18.30 Uhr</div></div>
  <div class="row"><div class="c1">4. Tag</div><div class="t2">09.00 – 13.00 Uhr</div></div>
</section>

<footer class="abs footer"><span style="left:127px">© 2021 Jonas Albrecht</span><span style="right:128px">Impressum | Datenschutz | AGB | Kontakt</span></footer>
</body>
</html>
```